carobrookcare needs a 4.6 handout

i need a styalized 4x6 postcard sized handout to leave on cars at shopping plazas and apartment buildings. WE are a medical marijuana referal clinic in brockton MA and we write perscriptions for qualifying patients, i have attached a pdf file of the content i need included in the hand out but please do not limit yourself if you feel like you could word it better. it is important to have our contact info front and center
Target Market(s)
potential medical marijuana patients
Industry/Entity Type
Apartment
Requirements
Must have
- the content listed inside the PDF file i attached
Nice to have
- must have everything in the PDF file. should be colorful and eye catching while still looking professional
Should not have
- pictures of cannabis buds or flowering plants.

```html
<!DOCTYPE html>
<html lang="en">
<head>
<meta charset="utf-8">
<title>Carobrook Care – Medical Marijuana Evaluations Postcard</title>
<link rel="stylesheet" href="https://fonts.googleapis.com/css2?family=Bebas+Neue&family=Open+Sans:wght@400;700&display=swap">
<style>
  :root {
    --brand-blue: #1f86e6;
    --ink-dark: #2b2b2d;
    --ink-text: #1d1d1f;
    --panel-gray: #eceef1;
    --soft-white: #f7f8fa;
    --line-gray: #3a3a3c;
    --white: #ffffff;
  }
  * { box-sizing: border-box; margin: 0; padding: 0; }
  html, body { width: 1200px; height: 1200px; overflow: hidden; }
  body { background: #c9c9c9; font-family: "Open Sans", Arial, sans-serif; position: relative; }

  .postcard {
    position: absolute; left: 50px; top: 233px;
    width: 1100px; height: 734px;
    background: var(--soft-white);
    overflow: hidden;
    box-shadow: 0 20px 40px rgba(0,0,0,.25);
  }
  .postcard-shapes { position: absolute; inset: 0; }

  .headline {
    position: absolute; right: 26px; text-align: right;
    font-family: "Bebas Neue", Impact, sans-serif;
    letter-spacing: .5px; white-space: nowrap;
  }
  .headline--question { top: 46px; font-size: 42px; color: var(--ink-text); }
  .headline--offer { top: 114px; font-size: 46px; color: var(--white); }

  .hours {
    position: absolute; left: 132px; top: 262px; width: 246px;
    color: var(--white);
  }
  .hours-title { font-family: "Bebas Neue", Impact, sans-serif; font-size: 46px; color: var(--brand-blue); margin-bottom: 6px; }
  .hours-row { display: flex; justify-content: space-between; font-size: 26px; line-height: 44px; }

  .conditions {
    position: absolute; left: 455px; top: 512px; width: 480px;
    text-align: center; font-size: 23px; line-height: 31px; color: var(--ink-text);
  }

  .brand-name {
    position: absolute; left: 948px; top: 526px; width: 124px;
    text-align: center; font-size: 20px; font-weight: 700; color: var(--ink-dark);
  }

  .call-to-action {
    position: absolute; left: 60px; top: 638px;
    color: var(--white); font-weight: 700; font-size: 24px; line-height: 32px;
  }
  .contact-line {
    position: absolute; left: 545px; top: 668px;
    color: var(--white); font-weight: 700; font-size: 23px; white-space: nowrap;
  }
</style>
</head>
<body>
  <div class="postcard">
    <svg class="postcard-shapes" width="1100" height="734" viewBox="0 0 1100 734">
      <defs>
        <linearGradient id="herbGradient" x1="0" y1="0" x2="1" y2="0">
          <stop offset="0" stop-color="#d89a2a"/>
          <stop offset=".35" stop-color="#5d6e35"/>
          <stop offset="1" stop-color="#7c8a4a"/>
        </linearGradient>
        <linearGradient id="photoGradient" x1="0" y1="0" x2="0" y2="1">
          <stop offset="0" stop-color="#e6edf3"/>
          <stop offset="1" stop-color="#b9c9d8"/>
        </linearGradient>
        <linearGradient id="hoursGradient" x1="0" y1="0" x2="0" y2="1">
          <stop offset="0" stop-color="#3b3b3e"/>
          <stop offset="1" stop-color="#232325"/>
        </linearGradient>
      </defs>

      <polygon points="380,0 1100,0 1100,210 470,210" fill="var(--panel-gray)"/>
      <rect x="470" y="210" width="630" height="420" fill="#f0f2f5" role="img" aria-label="Faded photo of a doctor in a white coat"/>

      <rect x="20" y="25" width="340" height="200" rx="10" fill="url(#herbGradient)" opacity=".85" role="img" aria-label="Photo of an orange prescription bottle spilling dried herbal medicine"/>

      <polygon points="360,0 385,0 490,245 465,245" fill="var(--brand-blue)"/>
      <polygon points="420,104 1100,104 1100,182 453,182" fill="var(--brand-blue)"/>

      <rect x="0" y="246" width="1100" height="5" fill="var(--brand-blue)"/>
      <rect x="0" y="240" width="1100" height="6" fill="var(--line-gray)"/>
      <line x1="1010" y1="250" x2="1100" y2="200" stroke="var(--line-gray)" stroke-width="10"/>

      <rect x="100" y="232" width="310" height="340" rx="30" fill="url(#hoursGradient)"/>
      <path d="M380,232 h30 q18,0 18,20 v18 q-12,-20 -48,-18 z" fill="#8a8a8c"/>

      <circle cx="560" cy="395" r="104" fill="var(--white)" stroke="var(--brand-blue)" stroke-width="9"/>
      <circle cx="560" cy="395" r="92" fill="url(#photoGradient)" role="img" aria-label="Photo of a senior doctor working at a desk"/>
      <circle cx="965" cy="320" r="100" fill="var(--white)" stroke="var(--brand-blue)" stroke-width="9"/>
      <circle cx="965" cy="320" r="88" fill="url(#photoGradient)" role="img" aria-label="Photo of a smiling young doctor with a stethoscope"/>
      <circle cx="765" cy="360" r="120" fill="var(--white)" stroke="var(--brand-blue)" stroke-width="9"/>
      <circle cx="765" cy="360" r="108" fill="url(#photoGradient)" role="img" aria-label="Photo of a doctor writing on a clipboard"/>

      <polygon points="410,642 1100,612 1100,734 410,734" fill="var(--ink-dark)"/>
      <line x1="410" y1="638" x2="1100" y2="608" stroke="var(--brand-blue)" stroke-width="4"/>
      <polygon points="0,612 440,590 505,734 0,734" fill="var(--brand-blue)"/>

      <circle cx="1010" cy="540" r="62" fill="var(--white)" stroke="#c9ccd0" stroke-width="5"/>
    </svg>

    <div class="headline headline--question">Do you need a medical marijuana card?</div>
    <div class="headline headline--offer">We do medical marijuana evaluations!</div>

    <div class="hours">
      <div class="hours-title">Hours:</div>
      <div class="hours-row"><span>Tuesday:</span><span>9-5</span></div>
      <div class="hours-row"><span>Wednesday:</span><span>9-5</span></div>
      <div class="hours-row"><span>Thursday:</span><span>9-6</span></div>
      <div class="hours-row"><span>Friday:</span><span>9-7</span></div>
      <div class="hours-row"><span>Saturday:</span><span>9-3</span></div>
    </div>

    <p class="conditions">There are over 200 qualifying conditions in the state of Massachusetts</p>

    <div class="brand-name">Carobrook</div>

    <p class="call-to-action">Call today to see if you qualify<br>and book an appointment!</p>
    <p class="contact-line">Www.Carobrookcare.Net | 555-014-2739</p>
  </div>
</body>
</html>
```